Brindlewood Holdings LLC - Business Cards

Need the following information on the cards:

Name: Marcus T Velding
Title: Chief Executive Manager

Business address:
412 N Pickerel Ridge Road #118
Fenwick Falls, Il 60999

Phone: (555) 481-0362 - Business
BRX FFL license number: 5-81-xxx-xx-xx-04519
Email: marcus.velding@brindlewoodholdingsffl.example

Target Market(s)

Firearm owners

Industry/Entity Type

Firearms industry,

Contact Information for Business Card

Contact number, name and title, web page address, email, business address and brx license number,

Requirements
Must have
• Name, title, business address, phone numbers, BRX license numbers, web page address and email address.
Nice to have
• Cellphone number,

```html
<!DOCTYPE html>
<html lang="en">
<head>
<meta charset="utf-8">
<title>Brindlewood Holdings LLC – Business Cards</title>
<link href="https://fonts.googleapis.com/css2?family=Montserrat:wght@400;500;700;800&display=swap" rel="stylesheet">
<style>
  :root {
    --bg: #3a3a3a;
    --card-black: #161616;
    --card-white: #ffffff;
    --red: #d42027;
    --charcoal: #3b3b3b;
    --ink: #222222;
    --white: #ffffff;
  }
  * { box-sizing: border-box; margin: 0; padding: 0; }
  html, body { width: 1200px; height: 1186px; overflow: hidden; }
  body {
    background: var(--bg);
    font-family: "Montserrat", sans-serif;
    position: relative;
  }
  .card {
    position: absolute;
    left: 160px;
    width: 880px;
    height: 503px;
    border-radius: 28px;
    overflow: hidden;
  }
  .card--back { top: 70px; background: var(--card-black); }
  .card--front { top: 613px; background: var(--card-white); }

  .brand-mark {
    position: absolute;
    display: flex;
    flex-direction: column;
    align-items: center;
    justify-content: center;
    text-align: center;
    border-radius: 50%;
    font-weight: 800;
    text-transform: uppercase;
    letter-spacing: 1px;
  }
  .card--back .brand-mark {
    left: 250px; top: 62px;
    width: 380px; height: 380px;
    border: 6px solid var(--white);
    color: var(--red);
    font-size: 36px;
    line-height: 1.15;
  }
  .card--front .brand-mark {
    left: 560px; top: 30px;
    width: 250px; height: 250px;
    border: 4px solid var(--ink);
    color: var(--red);
    font-size: 22px;
    line-height: 1.2;
  }

  .rule-top {
    position: absolute;
    left: 300px; right: 0; top: 304px;
    height: 2px; background: var(--red);
  }
  .address {
    position: absolute;
    right: 40px; top: 318px;
    text-align: right;
    font-size: 16px;
    line-height: 1.4;
    color: var(--ink);
  }
  .person {
    position: absolute;
    left: 44px; top: 336px;
  }
  .person__name {
    font-size: 26px;
    font-weight: 700;
    color: var(--red);
    text-transform: uppercase;
    letter-spacing: 0.5px;
  }
  .person__title {
    font-size: 16px;
    color: var(--ink);
    margin-top: 2px;
  }
  .person__rule {
    width: 260px; height: 2px;
    background: var(--red);
    margin-top: 10px;
  }
  .phone {
    position: absolute;
    left: 44px; top: 424px;
    display: flex; align-items: center; gap: 12px;
    font-size: 17px; font-weight: 700; color: var(--ink);
  }
  .bands { position: absolute; inset: 0; pointer-events: none; }
  .band-details {
    position: absolute;
    right: 34px; top: 408px;
    text-align: right;
    font-size: 14px;
    line-height: 24px;
    color: var(--white);
  }
</style>
</head>
<body>
  <section class="card card--back" aria-label="Card back">
    <div class="brand-mark">Brindlewood<br>Holdings LLC</div>
  </section>

  <section class="card card--front" aria-label="Card front">
    <div class="brand-mark">Brindlewood<br>Holdings LLC</div>

    <div class="rule-top"></div>
    <p class="address">412 N Pickerel Ridge Road #118<br>Fenwick Falls, Il 60999</p>

    <svg class="bands" width="880" height="503" viewBox="0 0 880 503" aria-hidden="true">
      <polygon points="400,398 880,398 880,503 0,503 0,488 350,488" fill="var(--red)"/>
      <polygon points="0,462 345,462 330,478 0,478" fill="var(--charcoal)"/>
    </svg>
    <div class="band-details">
      <p class="license">BRX FFL license number: 5-81-xxx-xx-xx-04519</p>
      <p class="email">marcus.velding@brindlewoodholdingsffl.example</p>
      <p class="web">www.brindlewoodholdingsffl.example</p>
    </div>

    <div class="person">
      <h1 class="person__name">Marcus T Velding</h1>
      <p class="person__title">Chief Executive Manager</p>
      <div class="person__rule"></div>
    </div>

    <div class="phone">
      <svg width="16" height="16" viewBox="0 0 24 24" aria-hidden="true">
        <path fill="var(--red)" d="M6.6 10.8a15.1 15.1 0 0 0 6.6 6.6l2.2-2.2c.3-.3.7-.4 1-.2 1.1.4 2.3.6 3.6.6.6 0 1 .4 1 1V20c0 .6-.4 1-1 1A17 17 0 0 1 3 4c0-.6.4-1 1-1h3.5c.6 0 1 .4 1 1 0 1.3.2 2.5.6 3.6.1.3 0 .7-.2 1z"/>
      </svg>
      <span>(555) 481-0362</span>
    </div>
  </section>
</body>
</html>
```